依頼詳細
<現状サイトの課題>
①一目で、何をしている会社なのかが分からない。
⇒商品画像・作業画像などを入れ、分かりやすく目を引き付けるようにする。

②項目が小さく、引き付けにくいデザイン。
⇒アイコンを大きくして、デザイン性を持たせる。

③自社の強みを視覚化できていない。
⇒図や写真を追加し、視覚的に伝わるようにする。

④自社の新着情報がないので社内の動きが把握できない。
⇒新着ニュースを追加し社内の動きが把握できるようにする。

⑤企業規模が小さく感じてしまう。
⇒洗練されたデザイン、コンテンツの充実、グローバルサイトの作成により企業規模をワンランク大きく見えるように表現する。
----------------------------------
<現在のサイト>
明確なサイトの情報共有はできませんが、TOPページの情報を一部伏せて共有します。添付の”TOPページ”をご参照ください。

<サイトリニューアルの方針>
①強みを明確にする為、全体的に画像化し打ち出したい。TOPページは動画を掲載し、よりリアルにユーザー様にイメージが伝わるデザインにする。

②企業規模をワンランク大きく見えるように表現し、グローバル化についてもアピールすることで、事業規模の大きい信頼出来る会社であることが分かるようにし、新規顧客の獲得および定着するようにサイトリニューアルを行う。

③必須機能
・TOPページへ動画を埋め込む。
・スマホ対応(レスポンシブウェブデザイン)にする。
・ウェブ見積り機能を設け、いつでも見積りが確認できるようにする。(TOPページにバナーを設けるなどデザインする)

<イメージ参考サイト>
①メインカラーをブルーとし、TOPページを開くとすぐに大きな画像イメージが見えます。
https://www.e-hariwa.co.jp/

②トップページに表示される、動画イメージです。
https://www.dovel.co.jp/

③コンテンツの配置や施工事例が見やすいです。
http://www.tasemi-kk.com/

④TOPページに施工写真や文字が挿入されており分かりやすい。また企業イメージがよく考えられており、ブランディングされています。
http://www.fujiyaga.co.jp/

<カラーテーマ>
①青系(堅実・信頼・クール)または水色系(さわやか・清潔感)

②青4割、白6割の配色のイメージでお願いします。制作の際は、カラーチャート(カラーを選んだ理由)もご提示いただけると幸いです。

<重視する点/検討基準>
①サイトコンセプトにあったデザイン(ご提案の際は、制作頂いたデザインコンセプト及びデザイン説明コメントの記載をお願い致します)

②納期厳守

<具体的な制作数>
TOPページ:1ページ(PC版のデザイン制作をお願いします)

<選考の進め方>
ご提案頂いたデザイン内容・コンセプトなどをもとに、プロジェクトメンバーで選考、決定致します。
※今回は、トップページデザインのみの見積りとなります。
今後、コーディングを依頼する可能性もございます。その場合は改めてクリエタスを通じてご依頼させて頂きます。パララックスデザインでのコーディングも条件として入れてまいります。
1ページ
青系、水色系
• イラストレーター形式 (.ai)
• フォトショップ形式 (.psd)
追記です。
サイトコンセプトの資料も添付いたします。
宜しくお願いいたします。

クライアント様と協議させていただき、コンセプトに合った総合的なデザインを評価させて頂きました。
その中で、クライアント様からの評価が多かった「Pixfern様」を当選とさせていただきました。ありがとうございました。

ランサーの皆さん、このように沢山の素敵なデザインをご提案頂き本当にありがとうございました。
コンセプトを基に、クライアント様とも大いに悩んで決定させて頂きました。
また、選定が期限間近になってしまいましたこと、申し訳ございませんでした。

機会があれば、今後ともどうぞ宜しくお願い致します。

```html
<!DOCTYPE html>
<html lang="ja">
<head>
<meta charset="utf-8">
<title>会社名 | 鉄製品の製作</title>
<link rel="stylesheet" href="https://fonts.googleapis.com/css2?family=Noto+Sans+JP:wght@400;500;700&family=Noto+Serif+JP:wght@600;700&display=swap">
<style>
:root{
  --blue:#1d62c8;
  --blue-dark:#0d3f93;
  --blue-light:#e6effb;
  --ink:#333;
  --muted:#777;
  --line:#d4d9e0;
  --gray:#ececec;
  --white:#fff;
}
*{box-sizing:border-box;margin:0;padding:0}
html,body{width:1200px;height:2930px;overflow:hidden}
body{font-family:"Noto Sans JP",sans-serif;color:var(--ink);background:var(--white);position:relative}
.wrap{width:840px;margin:0 auto;position:relative}

/* header */
.site-header{height:130px}
.brand{position:absolute;left:0;top:38px;display:flex;align-items:center;gap:14px}
.brand-mark{width:62px;height:50px;background:var(--blue);color:#fff;font-size:13px;display:flex;align-items:center;justify-content:center}
.brand-name{font-size:27px;font-weight:700;color:var(--blue-dark)}
.contact{position:absolute;right:0;top:26px;text-align:right}
.contact-label{font-size:12px;color:var(--blue);display:inline-block;border:1px solid var(--blue);padding:1px 8px}
.contact-tel{font-size:28px;font-weight:700;color:var(--blue);display:flex;align-items:center;justify-content:flex-end;gap:6px;margin-top:4px}
.contact-btn{display:inline-block;margin-top:6px;background:var(--blue);color:#fff;font-size:13px;padding:6px 14px}

.global-nav{height:70px;background:var(--blue)}
.global-nav ul{list-style:none;display:flex;width:840px;margin:0 auto}
.global-nav li{flex:1;color:#fff;font-size:12px;text-align:center;padding-top:12px;border-right:1px solid rgba(255,255,255,.3)}
.global-nav li:first-child{border-left:1px solid rgba(255,255,255,.3)}
.global-nav li.is-current{background:var(--blue-dark)}
.global-nav svg{display:block;margin:0 auto 6px}

/* hero */
.hero{height:440px;position:relative;background:linear-gradient(160deg,#0b2d72 0%,#2c78d8 40%,#a9cdf2 58%,#1d4fa8 78%,#0a2460 100%)}
.hero-copy{position:absolute;left:0;right:0;top:160px;text-align:center;color:#fff;font-family:"Noto Serif JP",serif;font-size:38px;font-weight:700;text-shadow:0 2px 8px rgba(0,0,40,.6)}

/* section titles */
.sec-title{text-align:center;font-family:"Noto Serif JP",serif;font-size:32px;font-weight:700;color:var(--ink)}
.sec-title::after{content:"";display:block;width:90px;height:3px;background:var(--blue);margin:12px auto 0}
.lead{font-size:12px;line-height:1.9;color:var(--muted);margin-top:26px}

.strengths{padding-top:40px}
.sub-title{text-align:center;font-family:"Noto Serif JP",serif;font-size:34px;color:var(--blue);margin-top:22px;font-style:italic}
.points{display:flex;justify-content:space-between;margin-top:26px}
.point{width:260px;text-align:center}
.point-circle{width:260px;height:260px;border-radius:50%;background:radial-gradient(circle at 35% 30%,#3d80dc,var(--blue) 60%,var(--blue-dark));position:relative;color:#fff;display:flex;align-items:center;justify-content:center}
.point-num{position:absolute;top:14px;left:0;right:0;font-size:90px;font-weight:700;color:rgba(255,255,255,.14)}
.point-text{position:relative;font-size:21px;font-weight:500;line-height:1.55}
.point-text em{font-style:normal;background:#fff;color:var(--blue);padding:0 6px}
.point-arrow{display:block;margin:14px auto 0}
.point-photo{height:160px;margin-top:14px;background:linear-gradient(135deg,#c9d2dd,#6f7f93 60%,#2d3a4c)}

/* works */
.works{padding-top:60px}
.works-strip{display:flex;margin-top:30px;height:220px;position:relative}
.works-strip div{flex:1;border-right:2px solid #fff}
.works-strip .w1{background:linear-gradient(180deg,#9fb3c9,#4b5f78)}
.works-strip .w2{background:linear-gradient(180deg,#dfe7ef,#8c9aab)}
.works-strip .w3{background:linear-gradient(180deg,#bfc9d4,#505a66)}
.works-strip .w4{background:linear-gradient(180deg,#5d7fa8,#1e2f4a)}
.works-strip .w5{background:linear-gradient(180deg,#d9e2ea,#7d8a99)}
.strip-arrow{position:absolute;top:90px;width:34px;height:40px;background:rgba(255,255,255,.8);display:flex;align-items:center;justify-content:center}

/* news */
.posts{display:flex;justify-content:space-between;margin-top:76px}
.post-col{width:400px}
.post-col .sec-title{font-size:28px}
.post-box{border:1px solid var(--line);margin-top:26px;padding:20px 22px 16px}
.post{display:flex;gap:12px;padding-bottom:14px;margin-bottom:14px;border-bottom:1px dotted var(--line)}
.post:last-of-type{border-bottom:none;margin-bottom:6px}
.post-side{width:80px}
.post-date{font-size:11px;color:var(--muted)}
.post-thumb{width:80px;height:56px;margin-top:6px;background:linear-gradient(135deg,#a8b8cc,#3c4c63)}
.post-body{flex:1}
.post-tag{display:inline-block;background:var(--blue);color:#fff;font-size:10px;padding:1px 10px}
.post-title{font-size:14px;font-weight:700;color:var(--blue);margin-top:4px}
.post-excerpt{font-size:11px;color:var(--muted);line-height:1.6;margin-top:2px}
.btn-more{display:inline-block;margin-top:8px;float:right;border:1px solid var(--blue);color:var(--blue);font-size:10px;padding:2px 10px}
.btn-list{display:block;width:96px;margin-left:auto;border:1px solid var(--blue);color:var(--blue);font-size:11px;padding:3px 0;text-align:center}
.to-top{position:absolute;right:0;top:2440px;width:70px;text-align:center;font-size:10px;color:var(--blue);border:1px solid var(--blue);padding:4px 0}
.to-top svg{display:block;margin:0 auto 2px}

/* footer */
.site-footer{position:absolute;left:0;right:0;top:2570px;height:310px;background:var(--gray)}
.footer-info{position:absolute;left:180px;top:40px}
.footer-info .brand{position:static}
.footer-tel{font-size:22px;font-weight:700;color:var(--blue);margin-top:22px;display:flex;align-items:center;gap:8px}
.footer-tel small{font-size:11px;font-weight:400;color:var(--muted)}
.footer-btn{display:block;width:220px;background:var(--blue);color:#fff;font-size:13px;padding:9px 16px;margin-top:12px}
.footer-map{position:absolute;left:500px;top:40px;width:520px;height:200px;background:linear-gradient(135deg,#eef0ec,#d5ddd2 50%,#c8d6e3)}
.footer-links{position:absolute;left:500px;top:252px;font-size:10px;color:var(--muted)}
.copyright{position:absolute;left:0;right:0;top:2880px;height:50px;background:var(--blue);color:#fff;font-size:11px;text-align:center;line-height:50px}
</style>
</head>
<body>
<header class="site-header wrap">
  <div class="brand"><span class="brand-mark">社名</span><span class="brand-name">会社名</span></div>
  <div class="contact">
    <span class="contact-label">お電話番号</span>
    <div class="contact-tel"><svg width="24" height="24" viewBox="0 0 24 24"><path fill="#1d62c8" d="M6.6 10.8a15 15 0 0 0 6.6 6.6l2.2-2.2a1 1 0 0 1 1-.3 11 11 0 0 0 3.6.6 1 1 0 0 1 1 1V20a1 1 0 0 1-1 1A17 17 0 0 1 3 4a1 1 0 0 1 1-1h3.5a1 1 0 0 1 1 1c0 1.3.2 2.5.6 3.6a1 1 0 0 1-.3 1z"/></svg>03-000-0000</div>
    <span class="contact-btn">お問合せ・ご見積りはこちら ▶</span>
  </div>
</header>

<nav class="global-nav">
  <ul>
    <li class="is-current"><svg width="22" height="20" viewBox="0 0 22 20"><path fill="#fff" d="M11 1 1 10h3v9h5v-6h4v6h5v-9h3z"/></svg>HOME</li>
    <li><svg width="22" height="20" viewBox="0 0 22 20"><rect x="2" y="5" width="18" height="13" fill="none" stroke="#fff" stroke-width="2"/><path d="M8 5V2h6v3" fill="none" stroke="#fff" stroke-width="2"/></svg>事業案内</li>
    <li><svg width="22" height="20" viewBox="0 0 22 20"><rect x="4" y="2" width="14" height="17" fill="none" stroke="#fff" stroke-width="2"/><path d="M8 7h6M8 11h6M8 15h6" stroke="#fff" stroke-width="2"/></svg>会社概要</li>
    <li><svg width="22" height="20" viewBox="0 0 22 20"><path fill="#fff" d="M11 1a6 6 0 0 0-6 6c0 5 6 12 6 12s6-7 6-12a6 6 0 0 0-6-6zm0 8a2 2 0 1 1 0-4 2 2 0 0 1 0 4z"/></svg>アクセス</li>
    <li><svg width="22" height="20" viewBox="0 0 22 20"><path d="M2 18h18M5 18V8l6-5 6 5v10" fill="none" stroke="#fff" stroke-width="2"/></svg>施工事例一覧</li>
    <li><svg width="22" height="20" viewBox="0 0 22 20"><circle cx="8" cy="7" r="3" fill="#fff"/><circle cx="15" cy="7" r="3" fill="#fff"/><path d="M2 18c0-4 3-6 6-6s6 2 6 6zM12 18c0-2 1-4 3-5 3 0 5 2 5 5z" fill="#fff"/></svg>社内風景</li>
    <li><svg width="22" height="20" viewBox="0 0 22 20"><path d="M2 3h18v11H9l-4 4v-4H2z" fill="none" stroke="#fff" stroke-width="2"/></svg>先輩の声</li>
    <li><svg width="22" height="20" viewBox="0 0 22 20"><path d="M3 17l2-5L15 2l3 3L8 15z" fill="none" stroke="#fff" stroke-width="2"/></svg>ブログ</li>
  </ul>
</nav>

<section class="hero" role="img" aria-label="青いガラスと鉄骨の建築内観の写真">
  <p class="hero-copy">クオリティの高い鉄製品を、短納期でご提供いたします。</p>
</section>

<section class="strengths wrap">
  <h2 class="sec-title">当社の強み</h2>
  <p class="lead">当社は創業以来、鉄製品の加工と製作を通じてお客様のものづくりを支えてまいりました。熟練の職人と最新の設備により、高い品質と短い納期を両立しております。小さな部品から大型の構造物まで、ご要望に合わせた柔軟な対応をお約束いたします。どんなことでもお気軽にご相談ください。</p>
  <p class="sub-title">3つの強み</p>
  <div class="points">
    <div class="point">
      <div class="point-circle"><span class="point-num">1</span><p class="point-text"><em>「高品質・短納期」</em><br>でご満足いただける<br>サービス</p></div>
      <svg class="point-arrow" width="40" height="22" viewBox="0 0 40 22"><path d="M0 0h40L20 22z" fill="#1d62c8"/></svg>
      <div class="point-photo" role="img" aria-label="鉄骨構造を見上げた写真"></div>
    </div>
    <div class="point">
      <div class="point-circle"><span class="point-num">2</span><p class="point-text">何でもご相談<br>いただける<br>柔軟な体制</p></div>
      <svg class="point-arrow" width="40" height="22" viewBox="0 0 40 22"><path d="M0 0h40L20 22z" fill="#1d62c8"/></svg>
      <div class="point-photo" role="img" aria-label="打ち合わせをする社員の写真"></div>
    </div>
    <div class="point">
      <div class="point-circle"><span class="point-num">3</span><p class="point-text">常にお客様目線で<br>取り組み<br>成長し続ける姿勢</p></div>
      <svg class="point-arrow" width="40" height="22" viewBox="0 0 40 22"><path d="M0 0h40L20 22z" fill="#1d62c8"/></svg>
      <div class="point-photo" role="img" aria-label="資料を確認するビジネスの写真"></div>
    </div>
  </div>
</section>

<section class="works">
  <div class="wrap">
    <h2 class="sec-title">施工事例</h2>
    <p class="lead">当社が手がけた施工事例の一部をご紹介いたします。階段や手すり、鉄骨架台などさまざまな製品を製作しております。</p>
  </div>
  <div class="works-strip">
    <div class="w1" role="img" aria-label="鉄骨階段の施工写真"></div>
    <div class="w2" role="img" aria-label="屋内の手すり施工写真"></div>
    <div class="w3" role="img" aria-label="外階段の施工写真"></div>
    <div class="w4" role="img" aria-label="ガラス屋根の施工写真"></div>
    <div class="w5" role="img" aria-label="駅構内の階段施工写真"></div>
    <span class="strip-arrow" style="left:180px"><svg width="12" height="18" viewBox="0 0 12 18"><path d="M10 1 2 9l8 8" fill="none" stroke="#1d62c8" stroke-width="3"/></svg></span>
    <span class="strip-arrow" style="right:180px"><svg width="12" height="18" viewBox="0 0 12 18"><path d="M2 1l8 8-8 8" fill="none" stroke="#1d62c8" stroke-width="3"/></svg></span>
  </div>
</section>

<section class="posts wrap">
  <div class="post-col">
    <h2 class="sec-title">お知らせ</h2>
    <div class="post-box">
      <article class="post"><div class="post-side"><p class="post-date">2016/00/01</p><div class="post-thumb" role="img" aria-label="お知らせのサムネイル写真"></div></div><div class="post-body"><span class="post-tag">ニュース</span><p class="post-title">ここにタイトルが入ります</p><p class="post-excerpt">ここに本文の一部が入ります。ここに本文の一部が入ります。</p><span class="btn-more">続きを読む ▶</span></div></article>
      <article class="post"><div class="post-side"><p class="post-date">2016/00/01</p><div class="post-thumb" role="img" aria-label="お知らせのサムネイル写真"></div></div><div class="post-body"><span class="post-tag">トピックス</span><p class="post-title">ここにタイトルが入ります</p><p class="post-excerpt">ここに本文の一部が入ります。ここに本文の一部が入ります。</p><span class="btn-more">続きを読む ▶</span></div></article>
      <span class="btn-list">一覧を見る ▶</span>
    </div>
  </div>
  <div class="post-col">
    <h2 class="sec-title">ブログ</h2>
    <div class="post-box">
      <article class="post"><div class="post-side"><p class="post-date">2016/00/01</p><div class="post-thumb" role="img" aria-label="ブログのサムネイル写真"></div></div><div class="post-body"><span class="post-tag">ブログ</span><p class="post-title">ここにタイトルが入ります</p><p class="post-excerpt">ここに本文の一部が入ります。ここに本文の一部が入ります。</p><span class="btn-more">続きを読む ▶</span></div></article>
      <article class="post"><div class="post-side"><p class="post-date">2016/00/01</p><div class="post-thumb" role="img" aria-label="ブログのサムネイル写真"></div></div><div class="post-body"><span class="post-tag">ブログ</span><p class="post-title">ここにタイトルが入ります</p><p class="post-excerpt">ここに本文の一部が入ります。ここに本文の一部が入ります。</p><span class="btn-more">続きを読む ▶</span></div></article>
      <span class="btn-list">一覧を見る ▶</span>
    </div>
  </div>
</section>

<div class="wrap" style="position:absolute;left:180px;top:0"><span class="to-top"><svg width="14" height="8" viewBox="0 0 14 8"><path d="M1 7l6-6 6 6" fill="none" stroke="#1d62c8" stroke-width="2"/></svg>ページのトップへ</span></div>

<footer class="site-footer">
  <div class="footer-info">
    <div class="brand"><span class="brand-mark">社名</span><span class="brand-name">会社名</span></div>
    <p class="footer-tel"><svg width="20" height="20" viewBox="0 0 24 24"><path fill="#1d62c8" d="M6.6 10.8a15 15 0 0 0 6.6 6.6l2.2-2.2a1 1 0 0 1 1-.3 11 11 0 0 0 3.6.6 1 1 0 0 1 1 1V20a1 1 0 0 1-1 1A17 17 0 0 1 3 4a1 1 0 0 1 1-1h3.5a1 1 0 0 1 1 1c0 1.3.2 2.5.6 3.6a1 1 0 0 1-.3 1z"/></svg>03-000-0000 <small>平日9:00〜18:00</small></p>
    <span class="footer-btn">✉ お問合せはこちら</span>
    <span class="footer-btn">✎ お見積りはこちら</span>
  </div>
  <div class="footer-map" role="img" aria-label="会社周辺の地図"></div>
  <p class="footer-links">HOME ｜ 事業案内 ｜ 会社概要 ｜ アクセス ｜ 施工事例一覧 ｜ 社内風景 ｜ 先輩の声 ｜ ブログ</p>
</footer>
<div class="copyright">Copyright (C) 2016 会社名 All rights reserved.</div>
</body>
</html>
```